Gestaltung eines Merkblattes
Ein Entwurf, der genau meinen Vorstellungen entspricht. Eine Abwicklung, die schneller und professioneller nicht sein könnte. Die Kommunikation - sehr symphatisch und kundenorientiert. Resumee: Besser geht es nicht.
Zielgruppe
www.tierklang-analytik.de/ Medizinische Bioresonanzanalysen für Pferde. Die Kundschaft besteht hauptsächlich aus Frauen, Alter von 20- 55 Jahre.
Bei dem Projekt handelt es sich um die Gestaltung eines wichtigen Merkblattes, das jedem Kunde zusammen mit dem Befund der Analyse gemailt wird. Es enthält wichtige Informationen rund um die Bioresonanzanalyse und sollte als pdf- Datei vorliegen.
Aufgabenstellung
Kernproblem: Die Kunden lesen das Merkblatt gar nicht oder nicht sorgfältig. So entstehen viele Fragen in der Folge, die nicht notwendig wären.
Wir benötigen eine pdf- Datei, die zum Lesen anregt, gerne gelesen wird und in der die wichtigsten Aspekte in das Auge fallen. Diese wurden von mir in der Worddatei, die den Text enthält, rot markiert.
Der Text in schwarz ist deutlich weniger wichtig.
Ach ja, die Überschrift ist doof. 'Allgemeine Hinweise' das animiert nicht wirklich zum Lesen. Falls Sie eine griffige Idee haben, sehr gerne.

```html
<!DOCTYPE html>
<html lang="de">
<head>
<meta charset="utf-8">
<title>Merkblatt – Hufsinn Vital</title>
<link href="https://fonts.googleapis.com/css2?family=Fira+Sans+Condensed:wght@400;500;600&family=Fira+Sans:wght@400&display=swap" rel="stylesheet">
<style>
  :root {
    --backdrop: #d9d9d9;
    --paper: #ffffff;
    --olive: #aab56c;
    --olive-soft: #d7dcb6;
    --ink: #3c3c3c;
    --ink-soft: #555555;
  }
  * { box-sizing: border-box; margin: 0; padding: 0; }
  html, body { width: 1200px; height: 977px; overflow: hidden; }
  body {
    background: var(--backdrop);
    font-family: "Fira Sans Condensed", "Arial Narrow", sans-serif;
    color: var(--ink);
  }
  .sheet {
    position: absolute;
    left: 270px; top: 18px;
    width: 660px; height: 940px;
    background: var(--paper);
    padding: 22px 38px 24px;
    box-shadow: 0 2px 10px rgba(0,0,0,.12);
    overflow: hidden;
  }
  .sheet-header {
    display: flex;
    align-items: flex-start;
    height: 104px;
  }
  .brand {
    width: 160px;
    display: flex;
    align-items: center;
    gap: 8px;
    padding-top: 30px;
  }
  .brand-dot {
    width: 14px; height: 14px; border-radius: 50%;
    background: var(--olive);
    flex: none;
  }
  .brand-name {
    font-weight: 600;
    font-size: 17px;
    line-height: 1.05;
    color: var(--olive);
    text-transform: uppercase;
    letter-spacing: .04em;
  }
  .headline-block { flex: 1; }
  .headline-bar {
    height: 12px;
    background: var(--olive);
    margin-right: -38px;
  }
  .headline {
    margin-top: 18px;
    font-weight: 600;
    font-size: 22px;
    letter-spacing: .02em;
    color: var(--ink);
    text-transform: uppercase;
  }
  .section { margin-top: 16px; }
  .section-title {
    font-weight: 600;
    font-size: 16px;
    color: var(--olive);
    text-transform: uppercase;
    letter-spacing: .02em;
    margin-bottom: 8px;
  }
  .columns {
    display: grid;
    grid-template-columns: repeat(3, 1fr);
    column-gap: 22px;
  }
  .topic-title {
    font-weight: 500;
    font-size: 12px;
    color: var(--olive);
    text-transform: uppercase;
    letter-spacing: .02em;
    margin-bottom: 12px;
  }
  .topic p {
    font-family: "Fira Sans", sans-serif;
    font-size: 10.8px;
    line-height: 1.45;
    color: var(--ink-soft);
    text-align: justify;
    -webkit-hyphens: auto;
    hyphens: auto;
    margin-bottom: 8px;
  }
  .illustration {
    display: block;
    margin: 6px auto 0;
    border-radius: 4px;
    background: linear-gradient(135deg, var(--olive-soft), #eef0e0);
  }
  .illustration--hand { width: 64px; height: 44px; }
  .illustration--pipette { width: 32px; height: 42px; }
</style>
</head>
<body>
<main class="sheet">
  <header class="sheet-header">
    <div class="brand">
      <span class="brand-dot"></span>
      <span class="brand-name">Hufsinn Vital</span>
    </div>
    <div class="headline-block">
      <div class="headline-bar"></div>
      <h1 class="headline">Bitte zum Wohle Ihres Pferdes lesen!</h1>
    </div>
  </header>

  <section class="section">
    <h2 class="section-title">Was Sie zum Befund der Analyse wissen sollten</h2>
    <div class="columns">
      <article class="topic">
        <h3 class="topic-title">Medikamentengabe</h3>
        <p>Die empfohlenen Präparate können Sie, wenn nicht anders angegeben, in das normale Kraftfutter geben. Tropfen und Bachblüten bitte auf ein kleines Stück trockenes Brot, Zwieback, bei Pferden, die kein Getreide fressen dürfen, auf ein Stück Reiswaffel geben und dem Pferd direkt füttern.</p>
        <p>Basispulver muss nicht, wie vom Hersteller angegeben, in Wasser aufgelöst werden. Eine Gabe in das Kraftfutter, Heucobs etc. vermindert nicht die Wirkung.</p>
      </article>
      <article class="topic">
        <h3 class="topic-title">Keine Unterbrechungen</h3>
        <p>Bitte füttern Sie alle Präparate, außer es sind abweichende Empfehlungen vorhanden, ohne Unterbrechung, bis Ihnen das Ergebnis der ersten Nachtestung vorliegt.</p>
        <p>Pausen von mehr als zwei Tagen können zu Beginn der Behandlung die positive Entwicklung Ihres Pferdes beeinträchtigen.</p>
        <div class="illustration illustration--hand" role="img" aria-label="Zeichnung einer Hand, die Kügelchen reicht"></div>
      </article>
      <article class="topic">
        <h3 class="topic-title">Für wählerische Pferde</h3>
        <p>Falls Ihr Pferd sehr wählerisch ist bei der Zufütterung von Präparaten in Pellet- oder Pulverform, dann beginnen Sie mit einer sehr kleinen Dosierung von z. B. ½ Teelöffel und steigern diese sehr langsam.</p>
        <p>Bei trockenem Futter (Müsli, Pellets) sortieren manche Pferde gerne aus. Hier ist es sinnvoll, das Futter anzufeuchten, etwas Heucobs oder getreidefreies Mash dazuzugeben.</p>
      </article>
    </div>
  </section>

  <section class="section">
    <h2 class="section-title">Was Sie zur Nachtestung wissen sollten</h2>
    <div class="columns">
      <article class="topic">
        <h3 class="topic-title">Haarprobe und Feedback</h3>
        <p>Wir brauchen für die Nachtestung eine neue Haarprobe und ein kurzes Feedback zu der aktuellen Entwicklung Ihres Pferdes, Mähne genügt.</p>
      </article>
      <article class="topic">
        <h3 class="topic-title">Keine Eingangsbestätigung</h3>
        <p>Wir bestätigen den Eingang der Probe zur Nachtestung nicht. In regelmäßigen Abständen werden alle Befunde nachgetestet.</p>
      </article>
      <article class="topic">
        <h3 class="topic-title">Ergebnis per Mail</h3>
        <p>Wir senden Ihnen im Anschluss per Mail das neue Ergebnis mit einer aktualisierten Therapieempfehlung zu.</p>
      </article>
    </div>
  </section>

  <section class="section">
    <h2 class="section-title">Was Sie zur Bachblüten-Therapie wissen sollten</h2>
    <div class="columns">
      <article class="topic">
        <h3 class="topic-title">Bachblüten</h3>
        <p>Wenn die Therapieempfehlung eine Übersicht an Bachblüten enthält, dann spiegelt diese den seelischen Zustand Ihres Pferdes wieder, der von seinen aktuellen Lebensbedingungen, seiner körperlichen Belastung durch Krankheit und durch Abläufe in seiner Herde beeinflusst wird.</p>
        <div class="illustration illustration--pipette" role="img" aria-label="Zeichnung einer Tropfpipette"></div>
      </article>
      <article class="topic">
        <h3 class="topic-title">Seelischer Zustand</h3>
        <p>Erfahrungsgemäß bezieht sich die Darstellung der Blüten bei Pferden, die in einer Herde leben, häufig mehr auf die Gefühle des Pferdes gegenüber seinen Artgenossen als auf den Kontakt mit dem Menschen.</p>
        <p>Die meisten Apotheken kennen sich aus mit der Herstellung einer Bachblütenmischung, falls nicht, hier die Anleitung.</p>
      </article>
      <article class="topic">
        <h3 class="topic-title">Herstellung</h3>
        <p>In ein 30 ml Medizinfläschchen mit Tropfeinrichtung oder Pipette gibt man 10 ml Alkohol (Brandy oder Weinbrand), 20 ml Quellwasser oder stilles Mineralwasser (ohne Kohlensäure), kein destilliertes Wasser, und 2–3 Tropfen von jeder Blüte, die im Moment benötigt wird. Als Alternative zu Alkohol kann auch Obstessig eingesetzt werden.</p>
      </article>
    </div>
  </section>
</main>
</body>
</html>
```